Author needs a new book, Kindle and Audiobook cover design

I updated and re-edited a book I wrote 25 years ago but now realize the title and design did not get the job done. I am seeking a book, Kindle and audiobook design that will make me stand out. The final design will pop while being sensitive to the nature of the subject. The title of the book is Quiet Lanterns. Subtitle: Ways to Notice and Step Away From Harmful Circles While Keeping Steady Belief by Dorian T. Wexcombe. I am wanting to get the attention of people who have been damaged by a church relationship that started well but ended badly.
Updates

The book title is: Quiet Lanterns. The Subtitle is: Ways To Notice and Step Away From Harmful Circles While Keeping Steady Belief. The dimension is 6x9 (150 pages) and I am the author: Dorian T. Wexcombe

Target Market(s)

People with a church experience; church leadership. Religious abuse victims.

Industry/Entity Type

Christian

Font styles to use
Serif

Colors

Designer to choose colors to be used in the design.

Requirements
Nice to have
• I am not married to the Serif font if another design works better.

```html
<!DOCTYPE html>
<html lang="en">
<head>
<meta charset="utf-8">
<title>Quiet Lanterns — Dorian T. Wexcombe</title>
<link href="https://fonts.googleapis.com/css2?family=Cinzel:wght@500;600&family=Crimson+Text&display=swap" rel="stylesheet">
<style>
  :root {
    --page: #f4f4f2;
    --cover-light: #ffffff;
    --cover-mid: #d6d6d6;
    --cover-dark: #7c7c7c;
    --ink: #151515;
    --title-red: #b0141e;
    --title-red-deep: #6a0a0f;
    --grass-pale: rgba(200, 226, 160, 0.55);
    --grass: #7fb347;
    --grass-deep: #4f8a2a;
  }
  * { margin: 0; padding: 0; box-sizing: border-box; }
  html, body {
    width: 1111px;
    height: 1200px;
    overflow: hidden;
    background: var(--page);
  }
  .book-cover {
    position: absolute;
    left: 175px;
    top: 50px;
    width: 760px;
    height: 1100px;
    background:
      radial-gradient(ellipse 62% 58% at 50% 56%, var(--cover-light) 0%, var(--cover-light) 30%, var(--cover-mid) 72%, var(--cover-dark) 125%);
    overflow: hidden;
  }
  .cover-title { margin: 0; }
  .title {
    position: absolute;
    left: 0;
    width: 100%;
    text-align: center;
    font-family: "Cinzel", Georgia, serif;
    line-height: 1;
  }
  .title-top {
    top: 100px;
    font-size: 108px;
    font-weight: 500;
    letter-spacing: 4px;
    color: var(--ink);
  }
  .title-main {
    top: 222px;
    font-size: 112px;
    font-weight: 600;
    letter-spacing: 2px;
    background: linear-gradient(180deg, var(--title-red) 0%, var(--title-red-deep) 100%);
    -webkit-background-clip: text;
    background-clip: text;
    color: transparent;
  }
  .cover-artwork {
    position: absolute;
    left: 80px;
    top: 400px;
    width: 600px;
    height: 600px;
    background:
      radial-gradient(ellipse 50% 50% at 50% 55%,
        rgba(255,255,255,0) 0%,
        rgba(255,255,255,0) 48%,
        var(--grass-pale) 60%,
        var(--grass) 72%,
        var(--grass-deep) 78%,
        var(--grass) 84%,
        rgba(143,191,90,0) 96%);
    -webkit-mask-image: radial-gradient(ellipse 50% 50% at 50% 55%, #000 80%, transparent 100%);
    mask-image: radial-gradient(ellipse 50% 50% at 50% 55%, #000 80%, transparent 100%);
  }
  .subtitle {
    position: absolute;
    left: 220px;
    top: 545px;
    width: 320px;
    text-align: center;
    font-family: "Crimson Text", Georgia, serif;
    font-size: 33px;
    line-height: 1.17;
    color: var(--ink);
  }
  .author {
    position: absolute;
    left: 0;
    width: 100%;
    top: 1012px;
    text-align: center;
    font-family: "Cinzel", Georgia, serif;
    font-weight: 500;
    font-size: 40px;
    letter-spacing: 2px;
    color: var(--ink);
  }
</style>
</head>
<body>
  <main class="book-cover">
    <h1 class="cover-title">
      <span class="title title-top">QUIET</span>
      <span class="title title-main">LANTERNS</span>
    </h1>
    <div class="cover-artwork" role="img" aria-label="House outline made of green grass blades topped by a grass cross"></div>
    <p class="subtitle">Ways to Notice and Step Away From Harmful Circles While Keeping Steady Belief</p>
    <p class="author">DORIAN T. WEXCOMBE</p>
  </main>
</body>
</html>
```